Professional Photography Business cards

I need business cards that include my logo which I have uploaded. I run a photography business. I am open to ideas but I would like one side to have my logo and the other side to have my contact info. I don't have a website made but I do own a website domain. I have uploaded 2 different logo color schemes. My business colors are Blue, black , and white.

Business Name
Business Phone Number
Business Email
Business Website address
Instagram

Industry/Entity Type

Professional Photography

Contact Information for Business Card

Phone Number: 555-304-7826 email: info@tkale-studio.example Instagram: @t.kalestudio website doman- www.tkale-studio.example

Requirements
Must have
• I like the idea of a business card with a full black background front and back of card. My colors must include royal blue, black, and white

```html
<!DOCTYPE html>
<html lang="en">
<head>
<meta charset="utf-8">
<title>T.Kale Studio – Business Cards</title>
<link rel="stylesheet" href="https://fonts.googleapis.com/css2?family=Roboto+Slab:wght@300;700&display=swap">
<style>
  :root {
    --stage: #b0b0b0;
    --card-black: #000000;
    --pattern-tone: #0d0d0d;
    --royal-blue: #0a14a0;
    --royal-blue-bright: #1f33d6;
    --text-white: #ffffff;
    --text-soft: #c4c4c4;
  }
  html, body {
    margin: 0;
    padding: 0;
    width: 1200px;
    height: 900px;
    overflow: hidden;
    background: var(--stage);
  }
  .canvas {
    position: relative;
    width: 1200px;
    height: 900px;
    font-family: "Roboto Slab", Georgia, serif;
  }
  .card {
    position: absolute;
    left: 262px;
    width: 676px;
    height: 405px;
    overflow: hidden;
    background: var(--card-black);
  }
  .card__backdrop {
    position: absolute;
    inset: 0;
    background: radial-gradient(ellipse at 50% 50%, var(--pattern-tone) 0%, var(--card-black) 85%);
  }

  /* Front */
  .card--front {
    top: 29px;
    display: flex;
    align-items: center;
    justify-content: center;
  }
  .brand {
    position: relative;
    display: flex;
    align-items: center;
    gap: 22px;
  }
  .brand__dot {
    width: 64px;
    height: 64px;
    border-radius: 50%;
    background: var(--royal-blue-bright);
  }
  .brand__name {
    margin: 0;
    font-weight: 700;
    font-size: 58px;
    line-height: 1;
    color: var(--text-white);
    letter-spacing: 1px;
  }

  /* Back */
  .card--back {
    top: 466px;
    color: var(--text-white);
    text-align: center;
  }
  .contact {
    position: relative;
  }
  .contact__name {
    margin: 0;
    padding-top: 72px;
    font-weight: 700;
    font-size: 42px;
    line-height: 52px;
    letter-spacing: 0.5px;
  }
  .contact__rule {
    width: 335px;
    height: 3px;
    margin: 18px auto 0;
    background: var(--royal-blue);
    border: 0;
  }
  .contact__list {
    list-style: none;
    margin: 16px 0 0;
    padding: 0;
    font-weight: 300;
    font-size: 20px;
  }
  .contact__item {
    height: 42px;
    line-height: 42px;
  }
  .contact__label { color: var(--text-white); margin-right: 6px; }
  .contact__value { color: var(--text-white); }
  .contact__value--soft { color: var(--text-soft); }
</style>
</head>
<body>
<main class="canvas">
  <section class="card card--front" aria-label="Card front">
    <div class="card__backdrop" aria-hidden="true"></div>
    <div class="brand">
      <span class="brand__dot" aria-hidden="true"></span>
      <h1 class="brand__name">T.Kale Studio</h1>
    </div>
  </section>

  <section class="card card--back" aria-label="Card back">
    <div class="card__backdrop" role="img" aria-label="Faint repeating camera aperture pattern on black"></div>
    <div class="contact">
      <h2 class="contact__name">T.KALE</h2>
      <hr class="contact__rule">
      <ul class="contact__list">
        <li class="contact__item"><span class="contact__label">Phone.</span> <span class="contact__value contact__value--soft">555-304-7826</span></li>
        <li class="contact__item"><span class="contact__label">Email.</span> <span class="contact__value">info@tkale-studio.example</span></li>
        <li class="contact__item"><span class="contact__label">Instagram.</span><span class="contact__value">@t.kalestudio</span></li>
        <li class="contact__item"><span class="contact__label">Website.</span> <span class="contact__value contact__value--soft">www.tkale-studio.example</span></li>
      </ul>
    </div>
  </section>
</main>
</body>
</html>
```